Referral Portal - Mobile App Design

To create a clean easy Web App Design for a Referral portal for Customer to submit and track their referrals.

Corvane Energy Referral Portal

https://www.corvane-energy.example

We are looking for a very simple phone app that will allow users to track their referrals. The sections/ things
We need in the app are as follows:
Form to Submit new Referrals
A very visual easy to read dashboard/ graph to show total Paid vs total potential(outstanding)
Simple Visual to show total paid
List of all referrals submitted and their status
Total number of referrals submitted and what Tier they fall into and what is the next tier (how close)

The App should be a minimal clean design that the user can navigate easily without much direction given.
This app should only be designed for the mobile experience. This is meant to gamify and incentives the user
To add more referrals and get more payments. Adding something fun with the Sun would be great!

Please See Linkup file for further information. We would like to name the App Corvane Energy Linkup

Thank you!!

Target Market(s)

Homeowners between ages of 30-60 who are familiar with apps that they use on their phone every day

Industry/Entity Type

Solar Energy

Font styles to use
Sans Serif

Colors
fbee3e
acd136
9bcb3c
f68e4e
f37022
f78f20
ffc214
34a7d8

Requirements
Must have
• Clean simple design, easy to use design/layout of nav.
• Visual charts and big graphic $$ on how much they have in their Wallet
• Easy visual to tell apart tiers (Gold, Silver,Platinum)
Nice to have
• Fun way to incorporate a rising or glowing sun
Should not have
• Too many words, not be bright and color

```html
<!DOCTYPE html>
<html lang="en">
<head>
<meta charset="utf-8">
<title>Corvane Energy Linkup – Dashboard</title>
<link href="https://fonts.googleapis.com/css2?family=Oswald:wght@300;400;500;600&family=Roboto:wght@300;400;700&family=Roboto+Condensed:wght@700&display=swap" rel="stylesheet">
<style>
  :root {
    --orange: #f37022;
    --green: #9bcb3c;
    --blue-text: #4a78a8;
    --blue-value: #3a6797;
    --blue-tile-top: #6fb3ea;
    --blue-tile-bottom: #3e77ae;
    --ink: #1c1c1c;
    --muted-tab: #a9a5a5;
    --tab-grey: #e2dede;
    --line: #dcdcdc;
    --brand-dot: #ffc214;
    --white: #ffffff;
  }
  * { box-sizing: border-box; margin: 0; padding: 0; }
  html, body { width: 1200px; height: 2329px; overflow: hidden; background: var(--white); }
  body { position: relative; font-family: "Roboto", Arial, sans-serif; color: var(--ink); }

  .topbar { position: absolute; left: 0; top: 0; width: 1200px; height: 93px; }
  .brand { position: absolute; left: 24px; top: 22px; display: flex; align-items: center; gap: 10px;
    font-weight: 400; font-size: 34px; color: #3a3a3a; }
  .brand-dot { width: 40px; height: 40px; border-radius: 50%; background: var(--brand-dot); }
  .welcome { position: absolute; right: 23px; top: 24px; font-size: 37px; font-weight: 400; }
  .welcome .logout { color: var(--orange); font-family: "Roboto Condensed", Arial, sans-serif; font-weight: 700; }

  .hero { position: absolute; left: 0; top: 93px; width: 1200px; height: 450px;
    background: linear-gradient(160deg, #3a3d42 0%, #24272b 55%, #1b1d20 100%); }
  .avatar { position: absolute; left: 39px; top: 42px; width: 342px; height: 342px; border-radius: 50%;
    border: 10px solid var(--orange); background: linear-gradient(180deg, #6b6b6b, #2f2f2f); }
  .balance-label { position: absolute; left: 419px; top: 80px; font-family: "Oswald", sans-serif; font-weight: 300;
    font-size: 54px; line-height: 1; color: var(--white); letter-spacing: -1px; }
  .balance-amount { position: absolute; left: 415px; top: 134px; font-family: "Oswald", sans-serif; font-weight: 600;
    font-size: 122px; line-height: 1; color: var(--orange); letter-spacing: -2px; }
  .btn { position: absolute; top: 315px; height: 89px; display: flex; align-items: center; justify-content: center;
    font-family: "Oswald", sans-serif; font-weight: 500; font-size: 46px; border-radius: 8px; }
  .btn-withdraw { left: 430px; width: 231px; border: 3px solid var(--orange); color: var(--orange); }
  .btn-earn { left: 688px; width: 239px; background: var(--orange); color: var(--white); }

  .stat-card { position: absolute; width: 552px; height: 380px; background: var(--white);
    border: 1px solid #e3e3e3; border-radius: 6px; box-shadow: 0 2px 6px rgba(0,0,0,.22); }
  .stat-icon { position: absolute; left: 22px; top: 57px; width: 222px; height: 225px; border-radius: 8px;
    background: linear-gradient(160deg, var(--blue-tile-top), var(--blue-tile-bottom));
    box-shadow: 3px 4px 6px rgba(0,0,0,.3); }
  .stat-text { position: absolute; left: 270px; top: 108px; }
  .stat-label { font-size: 28px; font-weight: 300; line-height: 1.28; color: var(--blue-text); text-transform: uppercase; }
  .stat-value { font-family: "Roboto Condensed", Arial, sans-serif; font-weight: 700; font-size: 41px; color: var(--blue-value); margin-top: 4px; }

  .tabs { position: absolute; left: 25px; top: 1397px; height: 86px; }
  .tab { position: absolute; top: 0; height: 86px; display: flex; align-items: center; justify-content: center;
    font-family: "Roboto Condensed", Arial, sans-serif; font-weight: 700; font-size: 43px; border-radius: 6px 6px 0 0; }
  .tab-paid { left: 0; width: 317px; color: var(--blue-value); background: var(--white); border: 1px solid var(--line); border-bottom: none; }
  .tab-paid span { border-bottom: 5px solid var(--blue-value); padding-bottom: 4px; }
  .tab-potential { left: 320px; width: 413px; color: var(--muted-tab); background: var(--tab-grey); }

  .referral-panel { position: absolute; left: 22px; top: 1483px; width: 1158px; height: 631px;
    border: 1px solid var(--line); border-radius: 8px; background: var(--white); }
  .col-head { position: absolute; top: 36px; font-size: 35px; font-weight: 300; color: var(--ink); }
  .col-company { left: 28px; }
  .col-tier { left: 444px; }
  .row { position: absolute; left: 0; width: 100%; height: 85px; }
  .row .company, .row .tier { position: absolute; top: 50%; transform: translateY(-50%); font-size: 44px; font-weight: 300; }
  .row .company { left: 30px; }
  .row .tier { left: 448px; }
  .upgrade { position: absolute; left: 681px; top: 0; width: 408px; height: 85px; background: var(--green);
    border-radius: 6px; color: var(--white); font-family: "Roboto Condensed", Arial, sans-serif; font-weight: 700;
    font-size: 27px; display: flex; align-items: center; justify-content: center; }
</style>
</head>
<body>

<header class="topbar">
  <div class="brand"><span class="brand-dot"></span>Corvane Energy</div>
  <div class="welcome">Welcome back, Marcus! <span class="logout">Logout?</span></div>
</header>

<section class="hero" role="img" aria-label="Aerial view of a neighbourhood with solar panels on rooftops">
  <div class="avatar" role="img" aria-label="Profile photo of the user"></div>
  <div class="balance-label">YOUR BALANCE IS USD</div>
  <div class="balance-amount">11,888.00</div>
  <div class="btn btn-withdraw">WITHDRAW</div>
  <div class="btn btn-earn">EARN MORE</div>
</section>

<div class="stat-card" style="left:25px; top:571px;">
  <div class="stat-icon" role="img" aria-label="Sun icon with a dollar sign"></div>
  <div class="stat-text"><div class="stat-label">Total earning<br>this month</div><div class="stat-value">USD 1,856</div></div>
</div>

<div class="stat-card" style="left:619px; top:571px;">
  <div class="stat-icon" role="img" aria-label="Sun icon with a checkmark"></div>
  <div class="stat-text"><div class="stat-label">Total paid<br>referrals</div><div class="stat-value">567</div></div>
</div>

<div class="stat-card" style="left:25px; top:992px;">
  <div class="stat-icon" role="img" aria-label="Sun icon"></div>
  <div class="stat-text" style="top:88px;"><div class="stat-label">Total potential<br>referrals</div><div class="stat-value">1058</div></div>
</div>

<div class="stat-card" style="left:619px; top:992px;">
  <div class="stat-icon" role="img" aria-label="Group of people icon"></div>
  <div class="stat-text" style="top:88px;"><div class="stat-label">Total shares</div><div class="stat-value">5023</div></div>
</div>

<nav class="tabs">
  <div class="tab tab-paid"><span>PAID REFERRAL</span></div>
  <div class="tab tab-potential">POTENTIAL REFERRAL</div>
</nav>

<section class="referral-panel">
  <div class="col-head col-company">COMPANY</div>
  <div class="col-head col-tier">TIER</div>

  <div class="row" style="top:104px;"><span class="company">ABC Company</span><span class="tier">Tier 1</span><div class="upgrade">CONTACT CLIENT TO UPGRADE</div></div>
  <div class="row" style="top:216px;"><span class="company">DEF Company</span><span class="tier">Tier 2</span><div class="upgrade">CONTACT CLIENT TO UPGRADE</div></div>
  <div class="row" style="top:334px;"><span class="company">XYZ Company</span><span class="tier">Tier 3</span></div>
  <div class="row" style="top:439px;"><span class="company">ABC Company</span><span class="tier">Tier 1</span><div class="upgrade">CONTACT CLIENT TO UPGRADE</div></div>
</section>

</body>
</html>
```